ALL TEXT GRAPHICS RK May 2025 for Instagram

We are looking for a series of social media graphics for Instagram (new size: 4:5 (1080 x 1350 pixels) ratio that are ALL TEXT. We want the following quotes below on each graphic; one quote per graphic. AND, In very small letters at the bottom of each graphic, add @RKBexleyOnline
The look and feel of these graphics should be complimentary to the color palette attached below; but keep them simple. But the design is up to you; at the end of this document, I provided various samples of all text graphics that I like as examples.
women looking to lose weight

```html
<!DOCTYPE html>
<html lang="en">
<head>
<meta charset="utf-8">
<title>Flat tummy in your 40s? — RK Bexley</title>
<link rel="stylesheet" href="https://fonts.googleapis.com/css2?family=Abril+Fatface&family=Italiana&family=Libre+Caslon+Text&display=swap">
<style>
  :root {
    --page: #ffffff;
    --panel: #faf3f7;
    --magenta: #cf0066;
    --ink: #0b0b0b;
    --muted: #6a6a6f;
  }
  html, body {
    margin: 0;
    padding: 0;
    width: 1200px;
    height: 1200px;
    overflow: hidden;
    background: var(--page);
  }
  .canvas {
    position: relative;
    width: 1200px;
    height: 1200px;
    background: var(--page);
  }
  .post {
    position: absolute;
    left: 120px;
    top: 0;
    width: 960px;
    height: 1200px;
    background: var(--panel);
  }
  .headline {
    position: absolute;
    left: 166px;
    top: 117px;
    margin: 0;
    font-family: "Abril Fatface", serif;
    font-weight: 400;
    font-size: 140px;
    line-height: 134px;
    letter-spacing: -1px;
    color: var(--magenta);
  }
  .call-to-action {
    position: absolute;
    left: 170px;
    top: 632px;
    margin: 0;
    font-family: "Italiana", serif;
    font-size: 86px;
    line-height: 106px;
    color: var(--ink);
  }
  .call-to-action .keyword {
    color: var(--magenta);
  }
  .handle {
    position: absolute;
    left: 160px;
    top: 1142px;
    margin: 0;
    font-family: "Libre Caslon Text", serif;
    font-size: 30px;
    line-height: 40px;
    color: var(--muted);
  }
</style>
</head>
<body>
  <main class="canvas">
    <section class="post">
    </section>
    <h1 class="headline">Flat tummy<br>in your<br>40s?</h1>
    <p class="call-to-action">Comment <span class="keyword">BYE BELLY</span> to<br>get the 10 secrets to<br>a flatter tummy</p>
    <p class="handle">@RKBexleyOnline</p>
  </main>
</body>
</html>
```